TBrenwick Business Cards & Letterhead

I have a logo but need a design for some new business cards. We are a Design-Build Firm that specializes in the design and construction of commercial projects.
the cards need to be professional. no cartoon stuff.
i would like to have the cards in AI format so I can update the card as needed. Logo is provided.
Our Address is: 4718 Fenmoor Ct. Dunmere, Vermont 05482

```html
<!DOCTYPE html>
<html lang="en">
<head>
<meta charset="utf-8">
<title>TBrenwick Business Cards</title>
<link rel="stylesheet" href="https://fonts.googleapis.com/css2?family=Arimo:wght@400;700&display=swap">
<style>
  :root {
    --backdrop: #e6e6e6;
    --card: #2e2e2f;
    --card-deep: #232324;
    --pattern-light: #4a4a4b;
    --accent: #0a6bb5;
    --text: #ffffff;
    --rule: #d9d9d9;
  }
  * { box-sizing: border-box; margin: 0; padding: 0; }
  html, body {
    width: 1200px; height: 801px; overflow: hidden;
    background: var(--backdrop);
    font-family: "Arimo", Arial, sans-serif;
  }
  .stage {
    position: relative; width: 1200px; height: 801px;
    display: flex; align-items: center; justify-content: center; gap: 40px;
  }
  .card {
    position: relative; width: 540px; height: 309px;
    background: var(--card); overflow: hidden;
    box-shadow: 0 6px 18px rgba(0,0,0,.22);
  }
  .brand {
    position: absolute; display: flex; align-items: center; gap: 10px;
    color: var(--text); font-weight: 700; letter-spacing: 1px; line-height: 1;
    white-space: nowrap;
  }
  .brand-mark { display: block; background: var(--accent); }
  .front .brand { top: 58px; left: 50%; transform: translateX(-50%); font-size: 34px; }
  .front .brand-mark { width: 22px; height: 22px; }
  .divider {
    position: absolute; left: 36px; right: 36px; top: 176px;
    height: 1px; background: var(--rule);
  }
  .person { position: absolute; left: 36px; top: 128px; }
  .person-name {
    color: var(--accent); font-weight: 700; font-size: 19px;
    letter-spacing: .5px; text-transform: uppercase;
  }
  .person-role { color: var(--text); font-size: 14px; margin-top: 3px; }
  .contacts { position: absolute; left: 36px; top: 192px; list-style: none; }
  .contact {
    display: flex; align-items: center; gap: 10px;
    color: var(--text); font-size: 13.5px; line-height: 1; margin-bottom: 10px;
    white-space: nowrap;
  }
  .contact svg { width: 13px; height: 13px; flex: none; }
  .address {
    position: absolute; right: 36px; top: 192px;
    color: var(--text); font-size: 14px; line-height: 1.45; font-style: normal;
    white-space: nowrap;
  }
  .back .pattern {
    position: absolute; inset: 0;
    background: linear-gradient(115deg, var(--card-deep) 0%, var(--card) 50%, var(--pattern-light) 100%);
  }
  .back .brand { right: 46px; bottom: 78px; font-size: 40px; }
  .back .brand-mark { width: 42px; height: 42px; }
</style>
</head>
<body>
<main class="stage">
  <section class="card front" aria-label="Business card front">
    <div class="brand"><span class="brand-mark"></span>TBRENWICK</div>
    <div class="person">
      <p class="person-name">Daniel Hayes</p>
      <p class="person-role">Manager</p>
    </div>
    <div class="divider"></div>
    <ul class="contacts">
      <li class="contact">
        <svg viewBox="0 0 16 16" aria-hidden="true"><path fill="#0a6bb5" d="M3.5 1.5l2.6 2.6-1.5 1.8c.9 2 2.5 3.6 4.5 4.5l1.8-1.5 2.6 2.6-1.8 2.5C6.8 13.6 2.4 9.2 1 3.3z"/></svg>
        555-318-4702
      </li>
      <li class="contact">
        <svg viewBox="0 0 16 16" aria-hidden="true"><rect x="1.5" y="3.5" width="13" height="9" fill="none" stroke="#0a6bb5" stroke-width="1.4"/><path d="M1.5 3.5l6.5 5 6.5-5" fill="none" stroke="#0a6bb5" stroke-width="1.4"/></svg>
        youremail@mailbox.com
      </li>
      <li class="contact">
        <svg viewBox="0 0 16 16" aria-hidden="true"><circle cx="8" cy="8" r="6.5" fill="none" stroke="#0a6bb5" stroke-width="1.4"/><path d="M1.5 8h13M8 1.5c-3 3.5-3 9.5 0 13M8 1.5c3 3.5 3 9.5 0 13" fill="none" stroke="#0a6bb5" stroke-width="1.2"/></svg>
        www.yourwebsite.com
      </li>
    </ul>
    <address class="address">4718 Fenmoor Ct.<br>Dunmere, Vermont 05482</address>
  </section>

  <section class="card back" aria-label="Business card back">
    <div class="pattern" role="img" aria-label="Embossed repeating brand-symbol pattern in dark and mid greys"></div>
    <div class="brand"><span class="brand-mark"></span>TBRENWICK</div>
  </section>
</main>
</body>
</html>
```